Business Card Design Project

KRV Management Consulting, LLC is a management consulting firm focused on improving an organization’s health and wellness while enhancing company performance with an emphasis on winning in the marketplace, profitable growth, team building, culture enablement and innovation.

Industry/Entity Type

Business

```html
<!DOCTYPE html>
<html lang="en">
<head>
<meta charset="utf-8">
<title>KRV Management Consulting, LLC — Business Card</title>
<link rel="stylesheet" href="https://fonts.googleapis.com/css2?family=Arimo:wght@400;700&family=Tinos:wght@400;700&family=Lato:wght@300&display=swap">
<style>
  :root {
    --page-bg: #141414;
    --card-bg: #272727;
    --text-light: #f2f2f2;
    --text-soft: #d9d9d9;
    --text-muted: #9a9a9a;
    --accent: #7cc242;
  }
  * { margin: 0; padding: 0; box-sizing: border-box; }
  html, body {
    width: 960px; height: 1200px; overflow: hidden;
    background: var(--page-bg);
    font-family: "Arimo", Arial, sans-serif;
  }
  .canvas { position: relative; width: 960px; height: 1200px; }
  .card {
    position: absolute; left: 80px; width: 800px; height: 457px;
    background: var(--card-bg); border-radius: 26px; overflow: hidden;
  }
  .card--front { top: 103px; }
  .card--back { top: 640px; }

  .brand { position: absolute; }
  .brand__name {
    font-family: "Tinos", "Times New Roman", serif; font-weight: 400;
    color: var(--text-light); line-height: 1; letter-spacing: 1px;
  }
  .brand__descriptor {
    font-family: "Lato", Arial, sans-serif; font-weight: 300;
    color: var(--text-muted); letter-spacing: 1px; white-space: nowrap;
  }
  .card--front .brand { left: 367px; top: 50px; }
  .card--front .brand__name { font-size: 75px; }
  .card--front .brand__descriptor { font-size: 26px; margin-top: 6px; }
  .card--back .brand { left: 438px; top: 36px; }
  .card--back .brand__name { font-size: 59px; }
  .card--back .brand__descriptor { font-size: 21px; margin-top: 4px; }

  .person { position: absolute; left: 41px; top: 54px; }
  .person__name {
    font-family: "Tinos", "Times New Roman", serif; font-weight: 700;
    font-size: 26px; color: var(--text-light); letter-spacing: .5px; line-height: 1;
  }
  .person__role { font-size: 18px; color: var(--accent); margin-top: 2px; }

  .divider {
    position: absolute; left: 41px; top: 323px; width: 716px; height: 1px;
    background: var(--accent);
  }
  .contacts {
    position: absolute; left: 41px; top: 348px; list-style: none;
    font-size: 19px; color: var(--text-soft); line-height: 25px;
  }
  .contacts li { display: flex; align-items: center; gap: 8px; }
  .contacts svg { width: 15px; height: 15px; flex: none; }
  .address {
    position: absolute; right: 43px; top: 376px; text-align: right;
    font-size: 19px; color: var(--text-soft); line-height: 25px;
  }

  .offerings__title {
    position: absolute; left: 40px; top: 42px;
    font-size: 19px; color: var(--accent); letter-spacing: .3px;
  }
  .services {
    position: absolute; left: 40px; top: 96px; list-style: none;
    font-size: 19px; color: var(--text-soft); line-height: 25px;
  }
  .services li { display: flex; align-items: center; }
  .services li::before {
    content: ""; width: 9px; height: 9px; border-radius: 50%;
    background: var(--accent); margin-right: 20px; flex: none;
  }
  .steps {
    position: absolute; top: 354px; list-style: none;
    font-size: 19px; color: var(--text-soft); line-height: 25px;
  }
  .steps--left { left: 40px; }
  .steps--right { left: 512px; }
  .steps li { display: flex; }
  .steps .num { color: var(--accent); margin-right: 3px; }
</style>
</head>
<body>
<main class="canvas">

  <section class="card card--front" aria-label="Business card front">
    <div class="person">
      <div class="person__name">DANIEL REYES</div>
      <div class="person__role">Managing Director</div>
    </div>
    <div class="brand">
      <div class="brand__name">KRV</div>
      <div class="brand__descriptor">Management Consulting, LLC</div>
    </div>
    <div class="divider"></div>
    <ul class="contacts">
      <li>
        <svg viewBox="0 0 16 16" aria-hidden="true"><rect x="4" y="1" width="8" height="14" rx="1.5" fill="none" stroke="#7cc242" stroke-width="1.6"/><line x1="7" y1="12.5" x2="9" y2="12.5" stroke="#7cc242" stroke-width="1.4"/></svg>
        (02) 5550 1842
      </li>
      <li>
        <svg viewBox="0 0 16 16" aria-hidden="true"><rect x="1" y="3" width="14" height="10" fill="#7cc242"/><path d="M1 3 L8 9 L15 3" fill="none" stroke="#272727" stroke-width="1.3"/></svg>
        hello@krvconsulting.com
      </li>
      <li>
        <svg viewBox="0 0 16 16" aria-hidden="true"><circle cx="8" cy="8" r="6.5" fill="#7cc242"/><path d="M1.5 8 H14.5 M8 1.5 C5 5 5 11 8 14.5 M8 1.5 C11 5 11 11 8 14.5" fill="none" stroke="#272727" stroke-width="1"/></svg>
        www.krvconsulting.com
      </li>
    </ul>
    <div class="address">
      PO BOX&nbsp; 48 Harbour Lane<br>
      5th street Geelong
    </div>
  </section>

  <section class="card card--back" aria-label="Business card back">
    <h2 class="offerings__title">SERVICE OFFERINGS</h2>
    <div class="brand">
      <div class="brand__name">KRV</div>
      <div class="brand__descriptor">Management Consulting, LLC</div>
    </div>
    <ul class="services">
      <li>Organizational Health Services</li>
      <li>Company Turnaround Services</li>
      <li>Innovation Lab Establishment</li>
      <li>Enterprise Risk Management</li>
      <li>Business Strategy Development</li>
      <li>Strategic Corporate Communication Strategy Development</li>
      <li>IT Strategy Development</li>
      <li>Complex Program and Project Management</li>
      <li>M&amp;A due diligence support</li>
      <li>Post-M&amp;A Integration Services including:</li>
    </ul>
    <ol class="steps steps--left">
      <li><span class="num">1.</span>Change Management</li>
      <li><span class="num">2.</span>Organization Design</li>
      <li><span class="num">3.</span>Integrated Business Strategy Development</li>
    </ol>
    <ol class="steps steps--right">
      <li><span class="num">4.</span>IT Integration Strategy<br>&nbsp;&nbsp;&nbsp;&nbsp;Development</li>
      <li><span class="num">5.</span>Leadership Development</li>
    </ol>
  </section>

</main>
</body>
</html>
```